Display board and Flyer Design

We are advertising our business in the local travel centre. We have a package where we get a lightbox (A1 - 594 x 841) and brochure display (either 2 x A4 or 4xDL). We would like to advertise Thornacre Lodge 1790 utilising the design for the gin label attached (minus the gin of course). We would also like to bring attention to the fact that the shop Wexmoor Apothecary Co is also at Thornacre Lodge as well as Garden and Gallery and gin tasting. For the brochure we are aiming to advertise everything we do at Thornacre Lodge, we would like the front to be the same as the above for the display board and the back similar to the Wexmoor Apothecary brochure that is also attached (essentially so the brochure could sit either way in the display stands. We would then like the internal pages of the brochure to highlight the garden, gallery, giftshop and gin tasting. I have attached another brochure that was designed for our wholesale market. I would like the brochure to have a similar look and feel as the Wexmoor Apothecary Co brochure utilising panama and helvetica nue fonts where able Once we have a basic design we can provide some more photography for specific elements i.e. Gin, gallery, giftshop, garden

Font styles to use
Other font styles liked:
• panama/ helvetica

Requirements
Must have
• similar feel to existing wexmoor apothecary co brochure
Nice to have
• similar fonts panama/helvetica nue
Should not have
• a design that is nothing like what our brand already is

```html
<!DOCTYPE html>
<html lang="en">
<head>
<meta charset="utf-8">
<title>Thornacre Lodge 1790 – Display Board</title>
<link rel="stylesheet" href="https://fonts.googleapis.com/css2?family=Arimo:wght@400;700&family=Young+Serif&display=swap">
<style>
  :root {
    --ink: #050505;
    --paper: #ffffff;
    --bar-fill: #0d0d0d;
    --rule: #d9d9d9;
    --stone-light: #6a6a6a;
    --stone-dark: #141414;
    --caption: #ffffff;
  }
  * { box-sizing: border-box; margin: 0; padding: 0; }
  html, body { width: 846px; height: 1200px; overflow: hidden; background: var(--ink); }
  .board { position: relative; width: 846px; height: 1200px; background: var(--ink); overflow: hidden; }

  .hero-photo {
    position: absolute; left: 0; top: 0; width: 846px; height: 690px;
    background:
      radial-gradient(ellipse 32% 10% at 22% 44%, rgba(190,190,190,.55), transparent 70%),
      radial-gradient(ellipse 22% 10% at 80% 46%, rgba(190,190,190,.5), transparent 70%),
      radial-gradient(ellipse 60% 55% at 50% 40%, #1a1a1a 0%, #0b0b0b 55%, transparent 100%),
      linear-gradient(90deg, #2b2b2b 0%, #0a0a0a 18%, #050505 50%, #0a0a0a 82%, #2b2b2b 100%);
    -webkit-mask-image: linear-gradient(180deg, #000 85%, transparent 100%);
            mask-image: linear-gradient(180deg, #000 85%, transparent 100%);
  }

  .brand-name {
    position: absolute; left: 300px; top: 110px; width: 260px;
    font-family: "Young Serif", serif; color: var(--paper);
    text-align: center; text-transform: uppercase; line-height: 1;
  }
  .brand-name .word { display: block; font-size: 38px; letter-spacing: 2px; }
  .brand-name .year { display: block; font-size: 150px; letter-spacing: -4px; margin: 14px 0 10px; }

  .intro {
    position: absolute; left: 0; width: 846px; top: 582px;
    font-family: "Young Serif", serif; font-size: 20px; line-height: 25px;
    color: var(--paper); text-align: center;
  }

  .info-bar {
    position: absolute; left: 130px; top: 710px; width: 585px; height: 65px;
    display: flex; border: 1px solid var(--paper); border-radius: 10px; overflow: hidden;
    font-family: "Arimo", sans-serif; color: var(--paper);
  }
  .info-bar .open {
    width: 173px; background: var(--paper); color: #222;
    font-weight: 700; font-size: 19px; display: flex; align-items: center; justify-content: center;
  }
  .info-bar .cell {
    background: var(--bar-fill); display: flex; flex-direction: column;
    align-items: center; justify-content: center; font-size: 19px; gap: 4px; padding-top: 2px;
  }
  .info-bar .hours { width: 149px; border-right: 1px solid var(--paper); }
  .info-bar .place { flex: 1; }
  .info-bar svg { width: 18px; height: 18px; }

  .features { position: absolute; left: 0; top: 828px; width: 846px; }
  .feature { position: absolute; top: 0; width: 236px; }
  .feature .crop { position: absolute; left: 0; top: 0; width: 236px; height: 236px; }
  .feature .photo { position: absolute; left: 14px; top: 17px; width: 208px; height: 208px; }
  .feature .caption {
    position: absolute; left: -20px; width: 276px; top: 245px;
    font-family: "Arimo", sans-serif; font-size: 19px; line-height: 21px;
    color: var(--caption); text-align: center; letter-spacing: -.3px;
  }
  .feature.garden { left: 59px; }
  .feature.gallery { left: 305px; }
  .feature.tasting { left: 550px; }
  .garden .photo { background: linear-gradient(160deg, #7a8b6a 0%, #4f6a3c 40%, #dfe3d4 75%, #9aa18c 100%); }
  .gallery .photo { background: linear-gradient(90deg, #6f6558 0%, #8a7d6c 30%, #7a4a2c 50%, #8a7d6c 70%, #5d6b3c 100%); }
  .tasting .photo { background: linear-gradient(135deg, #8b5a45 0%, #a06d58 35%, #4a2a1e 60%, #2a2420 80%, #b8bfc0 100%); }
</style>
</head>
<body>
<main class="board">
  <div class="hero-photo" role="img" aria-label="Black and white photo of hands gripping iron cell bars against a stone wall"></div>

  <h1 class="brand-name">
    <span class="word">Thornacre</span>
    <span class="year">1790</span>
    <span class="word">Lodge</span>
  </h1>

  <p class="intro">built (circa 1790) is the former home<br>of the Police Magistrate in Wexmoor.</p>

  <div class="info-bar">
    <div class="open">Now Open Daily</div>
    <div class="cell hours">
      <svg viewBox="0 0 24 24" fill="none" stroke="#fff" stroke-width="2"><circle cx="12" cy="12" r="10"/><path d="M12 6v6l3 2"/></svg>
      <span>10 am - 4 pm</span>
    </div>
    <div class="cell place">
      <svg viewBox="0 0 24 24" fill="none" stroke="#fff" stroke-width="2"><path d="M12 22s7-7 7-12a7 7 0 0 0-14 0c0 5 7 12 7 12z"/><circle cx="12" cy="10" r="2.5"/></svg>
      <span>27 Ferry Lane, Wexmoor</span>
    </div>
  </div>

  <section class="features">
    <article class="feature garden">
      <svg class="crop" viewBox="0 0 236 236"><g stroke="#d9d9d9" stroke-width="0.8"><line x1="0" y1="17" x2="236" y2="17"/><line x1="0" y1="225" x2="236" y2="225"/><line x1="14" y1="0" x2="14" y2="236"/><line x1="222" y1="0" x2="222" y2="236"/></g></svg>
      <div class="photo" role="img" aria-label="Garden bed with white hydrangeas and a dark urn"></div>
      <p class="caption">Wexmoor Apothecary<br>Co' Garden</p>
    </article>
    <article class="feature gallery">
      <svg class="crop" viewBox="0 0 236 236"><g stroke="#d9d9d9" stroke-width="0.8"><line x1="0" y1="17" x2="236" y2="17"/><line x1="0" y1="225" x2="236" y2="225"/><line x1="14" y1="0" x2="14" y2="236"/><line x1="222" y1="0" x2="222" y2="236"/></g></svg>
      <div class="photo" role="img" aria-label="Rusted metal sign on a weathered timber fence"></div>
      <p class="caption">Wexmoor Apothecary<br>Co' Gallery</p>
    </article>
    <article class="feature tasting">
      <svg class="crop" viewBox="0 0 236 236"><g stroke="#d9d9d9" stroke-width="0.8"><line x1="0" y1="17" x2="236" y2="17"/><line x1="0" y1="225" x2="236" y2="225"/><line x1="14" y1="0" x2="14" y2="236"/><line x1="222" y1="0" x2="222" y2="236"/></g></svg>
      <div class="photo" role="img" aria-label="Leather armchair beside a brick fireplace with framed prints"></div>
      <p class="caption">Wexmoor Apothecary<br>Gin Tasting</p>
    </article>
  </section>
</main>
</body>
</html>
```